New business card/stationary for a consulting company

I am looking for a clean and very professional looking business card for my consulting company as well as corresponding stationary. I am uploading our logo. I like simple and powerful for the feel. No graphics but I am open on everything else. Below is my contact information but would like the final to be in a version I can add my employees information into and print. Thank you.

Daniel Whitcombe
dan@fernlowadvisory.com
2837 North 9th Avenue, Summit Floor, Harlow Ridge, Ohio 60483
www.fernlowadvisory.com

Industry/Entity Type

Consulting

Contact Information for Business Card

Daniel Whitcombe
dan@fernlowadvisory.com
www.fernlowadvisory.com

Font styles to use
Serif
Sans Serif

Requirements
Must have
• Our logo and the business card details.
Nice to have
• our website www.fernlowadvisory.com

```html
<!DOCTYPE html>
<html lang="en">
<head>
<meta charset="utf-8">
<title>Fernlow Advisory – Business Card</title>
<link rel="stylesheet" href="https://fonts.googleapis.com/css2?family=Cinzel:wght@700&family=Source+Sans+3:wght@300;400;600&display=swap">
<style>
  :root {
    --stage: #2e2e2e;
    --paper: #ececec;
    --navy: #27245e;
    --navy-deep: #222056;
    --ink: #1c1c1c;
    --silver: #b9b9c4;
    --silver-dim: #9d9db0;
  }
  * { margin: 0; padding: 0; box-sizing: border-box; }
  html, body { width: 1200px; height: 600px; overflow: hidden; }
  body {
    background: var(--stage);
    font-family: "Source Sans 3", sans-serif;
    position: relative;
  }
  .card {
    position: absolute;
    top: 164px;
    width: 466px;
    height: 272px;
    border-radius: 17px;
    overflow: hidden;
  }
  .card--front { left: 123px; background: var(--paper); }
  .card--back  { left: 613px; background: var(--navy-deep); }

  /* front */
  .brand {
    position: absolute;
    left: 40px;
    top: 120px;
    display: flex;
    align-items: center;
    gap: 8px;
    color: var(--navy);
    font-weight: 600;
    font-size: 19px;
  }
  .brand__mark { width: 14px; height: 14px; background: var(--navy); }

  .person { position: absolute; left: 230px; top: 60px; }
  .person__name {
    font-family: "Cinzel", serif;
    font-weight: 700;
    font-size: 17px;
    color: var(--ink);
    letter-spacing: 0.3px;
    line-height: 1.1;
  }
  .person__title {
    font-family: "Cinzel", serif;
    font-weight: 700;
    font-size: 11px;
    color: var(--navy);
    line-height: 1.2;
  }

  .contacts { position: absolute; left: 230px; top: 112px; list-style: none; }
  .contacts li {
    position: relative;
    padding-left: 17px;
    font-size: 12px;
    line-height: 14px;
    color: var(--ink);
    margin-bottom: 8px;
  }
  .contacts svg { position: absolute; left: 0; top: 2px; width: 11px; height: 11px; fill: var(--navy); }
  .contacts svg.icon-line { fill: none; stroke: var(--navy); stroke-width: 1; }

  .social { position: absolute; left: 367px; top: 240px; display: flex; gap: 17px; }
  .social span { width: 14px; height: 14px; background: var(--navy); border-radius: 2px; }

  /* back */
  .back-mark {
    position: absolute;
    left: 219px; top: 96px;
    width: 28px; height: 28px;
    background: var(--silver);
  }
  .back-name {
    position: absolute;
    left: 0; right: 0; top: 148px;
    text-align: center;
    color: var(--silver);
    font-weight: 300;
    font-size: 27px;
    line-height: 32px;
    letter-spacing: 1px;
  }
  .back-web {
    position: absolute;
    left: 0; right: 0; top: 210px;
    text-align: center;
    color: var(--silver-dim);
    font-size: 10.5px;
  }
</style>
</head>
<body>
  <section class="card card--front">
    <div class="brand"><span class="brand__mark"></span>Fernlow Advisory</div>

    <div class="person">
      <p class="person__name">Daniel Whitcombe</p>
      <p class="person__title">Job Title</p>
    </div>

    <ul class="contacts">
      <li>
        <svg viewBox="0 0 12 12"><path d="M1 3h10v7H1z"/><path d="M1 3.5l5 3.5 5-3.5" fill="none" stroke="#ececec" stroke-width="0.9"/></svg>
        dan@fernlowadvisory.com
      </li>
      <li>
        <svg viewBox="0 0 12 12"><path d="M1 4c0-2 2-3 5-3s5 1 5 3v1H8V4H4v1H1z"/><rect x="2" y="6" width="8" height="5" rx="1"/></svg>
        000 000 0000
      </li>
      <li>
        <svg viewBox="0 0 12 12"><path d="M6 0a4 4 0 0 0-4 4c0 3 4 8 4 8s4-5 4-8a4 4 0 0 0-4-4zm0 5.5A1.5 1.5 0 1 1 6 2.5a1.5 1.5 0 0 1 0 3z"/></svg>
        2837 North 9th Avenue<br>Summit Floor, Harlow Ridge, Ohio 60483
      </li>
      <li>
        <svg class="icon-line" viewBox="0 0 12 12"><circle cx="6" cy="6" r="5"/><ellipse cx="6" cy="6" rx="2.2" ry="5"/><path d="M1 6h10M2 3.5h8M2 8.5h8"/></svg>
        www.fernlowadvisory.com
      </li>
    </ul>

    <div class="social" aria-label="Social profiles">
      <span></span><span></span><span></span>
    </div>
  </section>

  <section class="card card--back">
    <div class="back-mark"></div>
    <p class="back-name">FERNLOW ADVISORY</p>
    <p class="back-web">www.fernlowadvisory.com</p>
  </section>
</body>
</html>
```